Business Card Design

We would like a business card that utilizes our current logo and keeps with the same feel - elegant and organic. Our farm isn't about mass production, it's about excellence, education, beautiful events and flowers - people, culture, and community.

Target Market(s)

Patrons to our farm who are interested in weddings, events, or our flowers and vegetables.

Contact Information for Business Card

Name, address, cell email (Danielle Hoskins, 2716 Wrenfield Rd, Larkmoor, CO 81250, cell 30.412.6638, email danielle@wrenfieldacres.com)

```html
<!DOCTYPE html>
<html lang="en">
<head>
<meta charset="utf-8">
<title>Wrenfield Acres – Business Card</title>
<link href="https://fonts.googleapis.com/css2?family=Roboto:wght@400;500&display=swap" rel="stylesheet">
<style>
  :root {
    --sage: #768a76;
    --earth: #a57f57;
    --ink: #222222;
    --paper: #ffffff;
    --backdrop: #efefed;
  }
  * { box-sizing: border-box; margin: 0; padding: 0; }
  html, body {
    width: 1200px; height: 896px; overflow: hidden;
    background: var(--backdrop);
    font-family: "Roboto", Arial, sans-serif;
    color: var(--ink);
  }
  .card {
    position: absolute;
    left: 334px;
    width: 527px; height: 302px;
    background: var(--paper);
    border-radius: 29px;
    overflow: hidden;
  }
  .card--front { top: 125px; }
  .card--back { top: 471px; }

  .brand {
    position: absolute;
    display: flex; align-items: center; gap: 8px;
    color: var(--sage);
    font-weight: 400;
    white-space: nowrap;
  }
  .brand__dot {
    border-radius: 50%;
    background: var(--sage);
    flex: none;
  }
  .card--front .brand {
    left: 40px; top: 132px;
    font-size: 24px;
  }
  .card--front .brand__dot { width: 10px; height: 10px; }

  .divider {
    position: absolute;
    left: 274px; top: 70px;
    width: 2px; height: 162px;
    background: var(--earth);
  }
  .details {
    position: absolute;
    left: 287px; top: 67px;
  }
  .details__name {
    font-size: 23px; font-weight: 500;
    color: var(--earth);
    line-height: 1;
  }
  .details__title {
    font-size: 12px; margin-top: 6px;
  }
  .details__address {
    font-size: 12px; line-height: 20px; margin-top: 20px;
  }
  .details__contacts {
    list-style: none; margin-top: 10px;
    font-size: 12px; line-height: 20px;
  }
  .details__contacts li { display: flex; align-items: center; gap: 4px; }
  .icon { width: 10px; height: 10px; fill: var(--earth); flex: none; }

  .footer-band {
    position: absolute; left: 0; right: 0; bottom: 0;
    height: 50px;
    background: linear-gradient(180deg, var(--sage) 0%, var(--sage) 40%, var(--earth) 60%, var(--earth) 100%);
  }

  .card--back .brand {
    left: 0; right: 0; top: 0; bottom: 0;
    justify-content: center;
    font-size: 50px; gap: 14px;
  }
  .card--back .brand__dot { width: 18px; height: 18px; }
</style>
</head>
<body>
  <section class="card card--front">
    <div class="brand"><span class="brand__dot"></span>Wrenfield Acres</div>
    <div class="divider"></div>
    <div class="details">
      <p class="details__name">Ruth Calloway</p>
      <p class="details__title">Managing Director</p>
      <p class="details__address">Danielle Hoskins, 2716 Wrenfield<br>Rd, Larkmoor, CO 81250</p>
      <ul class="details__contacts">
        <li><svg class="icon" viewBox="0 0 10 10"><path d="M2.5 0h5a1 1 0 0 1 1 1v8a1 1 0 0 1-1 1h-5a1 1 0 0 1-1-1V1a1 1 0 0 1 1-1zm.5 1.2v6.6h4V1.2z"/></svg>30.412.6638</li>
        <li><svg class="icon" viewBox="0 0 10 10"><path d="M0 2h10v.8L5 5.6 0 2.8zM0 3.8l5 2.8 5-2.8V8H0z"/></svg>info@wrenfieldacres.com</li>
        <li><svg class="icon" viewBox="0 0 10 10"><circle cx="5" cy="5" r="4.6"/></svg>www.wrenfieldacres.com</li>
      </ul>
    </div>
    <div class="footer-band" role="img" aria-label="Decorative sage and brown wave band"></div>
  </section>

  <section class="card card--back">
    <div class="brand"><span class="brand__dot"></span>Wrenfield Acres</div>
  </section>
</body>
</html>
```